Stylish, Masculine Design - Men's Clothing

Granary Coat Mart is a 14,000 square foot warehouse outlet store open to the public since 2005. 50+ brands. Well-known designer brand names and private labels. 30-80% off retail everyday. Lowest prices guaranteed. Average suit price $150. Average shirt price $20. One-stop shop shopping. Men's suits, tuxedos, tuxedo rentals, dress shirts, ties, dress shoes, boy's suits and tuxedos, clergy robes, clergy shirts, cologne, loungewear. Slim fits (Prom Dance), business styles, "church" fashion, security-related uniform. Alterations done by expert tailors on premises for an extra charge.
The final design for both business card and logo should portray stylishness and masculinity.
Updates
We will be changing our name. Details below.New name: Granary Coat & Vest name: Granary Coat Mart Added Monday, December 26, 2016
Target Market(s)
Gender: 80% Male, 15% Female, 5% Transgender
Location: 80% 10 Mile Radius, 20% >10 Mile Radius
Age: 17-18 (Primarily prom), 18-35 (Primarily Interviews and Weddings), 36-70 (primarily Church and events)
Race: African-American 50%, Latino-American 20%, White 15%, 10% Asian 5% Other
Religions: Christian 50%, 20% Catholic, 10% Mormon, 20% Other/None
Occupation: Local government 40%, Large corporation employee 20%, Small business employee 10%, Small business owner 10%, 20% Unemployed (high school, college)
Education: High School or equivalent 40%, College 30%, Some College 20%, Masters/Doctors 10%
Industry/Entity Type
Retail
Contact Information for Business Card
Name: Peter Olund
Title: Sales Associate
Address: 418 E. Mirabeth Ave. Gardena, CA 90247
Phone Number: 310.555.0182
Slogan: Warehouse Selection. Outlet Prices, Outstanding Service
www.granarycoatmart.example
Logo Text
GCM (Acronym for Granary Coat Mart) or Image
Requirements
Must have
- Easy to read
- Visually appealing

```html
<!DOCTYPE html>
<html lang="en">
<head>
<meta charset="utf-8">
<title>Granary Coat Mart – Business Card</title>
<link href="https://fonts.googleapis.com/css2?family=Open+Sans:wght@400;600;700&display=swap" rel="stylesheet">
<style>
  :root {
    --backdrop: #1b1b1c;
    --card: #2b2b2d;
    --white: #ffffff;
    --muted: #c9c9c9;
    --red: #e2232a;
    --divider: #6a6a6c;
  }
  * { margin: 0; padding: 0; box-sizing: border-box; }
  html, body {
    width: 1200px; height: 1000px; overflow: hidden;
    background: var(--backdrop);
    font-family: "Open Sans", Arial, sans-serif;
  }
  .card {
    position: absolute; left: 150px; top: 243px;
    width: 900px; height: 514px;
    background: var(--card);
    border-radius: 34px;
  }
  .brand {
    position: absolute; left: 70px; top: 200px; width: 300px;
    display: flex; align-items: center; gap: 14px;
  }
  .brand-dot {
    flex: none; width: 22px; height: 22px; border-radius: 50%;
    background: var(--red);
  }
  .brand-name {
    color: var(--white); font-weight: 600; font-size: 32px;
    line-height: 1.15; letter-spacing: 0.5px; white-space: nowrap;
  }
  .divider {
    position: absolute; left: 400px; top: 80px;
    width: 1px; height: 250px; background: var(--divider);
  }
  .contact { position: absolute; left: 432px; top: 78px; }
  .person-name {
    color: var(--white); font-weight: 700; font-size: 30px;
    letter-spacing: 0.5px; line-height: 1.1;
  }
  .person-title { color: var(--red); font-size: 21px; margin-top: 4px; }
  .address {
    color: var(--muted); font-size: 19px; line-height: 1.3; margin-top: 14px;
  }
  .channels { list-style: none; margin-top: 14px; }
  .channel {
    display: flex; align-items: center; gap: 16px;
    color: var(--muted); font-size: 19px; line-height: 1.55;
  }
  .channel svg { width: 16px; height: 16px; flex: none; fill: var(--red); }
  .accent { color: var(--red); }
  .slogan {
    position: absolute; left: 0; right: 0; bottom: 58px;
    text-align: center; color: var(--muted); font-size: 20px;
    letter-spacing: 0.3px;
  }
</style>
</head>
<body>
  <main class="card">
    <div class="brand">
      <span class="brand-dot"></span>
      <span class="brand-name">Granary Coat<br>&amp; Vest</span>
    </div>

    <div class="divider"></div>

    <section class="contact">
      <h1 class="person-name">PETER OLUND</h1>
      <p class="person-title">Sales Associate</p>
      <p class="address">418 E. Mirabeth Ave.<br>Gardena, CA 90247</p>
      <ul class="channels">
        <li class="channel">
          <svg viewBox="0 0 16 16" aria-hidden="true"><path d="M3.6 1.2l2.3 2.6-1.3 2a8.5 8.5 0 0 0 5.6 5.6l2-1.3 2.6 2.3-1.3 2.1C8 15.6.4 8 .9 2.5z"/></svg>
          <span>310 555 0182</span>
        </li>
        <li class="channel">
          <svg viewBox="0 0 16 16" aria-hidden="true"><path d="M1 3h14v1.2L8 9 1 4.2z"/><path d="M1 6l7 4.8L15 6v7H1z"/></svg>
          <span>peter@granarycoatmart.example</span>
        </li>
        <li class="channel">
          <svg viewBox="0 0 16 16" aria-hidden="true"><path d="M8 1a7 7 0 1 0 0 14A7 7 0 0 0 8 1zm-.8 1.7v2.6H4.9c.5-1.3 1.3-2.3 2.3-2.6zm1.6 0c1 .3 1.8 1.3 2.3 2.6H8.8zM3.2 6.8h4v2.4h-4a6 6 0 0 1 0-2.4zm5.6 0h4a6 6 0 0 1 0 2.4h-4zm-3.9 3.9h2.3v2.6c-1-.3-1.8-1.3-2.3-2.6zm3.9 0h2.3c-.5 1.3-1.3 2.3-2.3 2.6z"/></svg>
          <span>www.<span class="accent">granarycoatmart</span>.example</span>
        </li>
      </ul>
    </section>

    <p class="slogan">Wide Range | Fair Prices | Expert Tailoring</p>
  </main>
</body>
</html>
```